Anzeigengestaltung für Bewerbung einer Immobilie
Zielgruppe
Ich bin als Immobilienmakler (VWR zertifiziert) tätig und bewerte und vermesse Immobilien für meine Kunden. Zielgruppe sind Personen, die ein Haus kaufen möchten.
Ich benötige eine Zeitungsannonce die sich vom Rest der Anzeigen abhebt und durch geeigneten Eyecatcher und Farbe auffällt. Ob durch Rahmen, Farbe oder Maskottchen überlasse ich gerne Ihnen. WICHTIG: Die Anzeige wird auf den ersten Blick gut erkannt.
Aufgabenstellung
Die Annonce soll eine Immobilie bewerben, die aktuell im Verkauf steht. Für mich wichtig, ich benötige eine Vorlage die ich selber bearbeiten kann. Ich möchte das Bild der, zum Verkauf stehenden, Immobilie, den Werbetext, die Überschrift, sowie den Preis anpassen können. Die Anzeige ist aktuell 90x90 mm groß und wird farbig gedruckt. Ein Logo liegt in geeigneter Qualität vor.
Ich stelle mir vor, das ich ein Foto vom Haus abbilde und 3-4 kleine Werbetexte, bestehend aus 4-7 Wörtern einblende. Dazu eine auffällige knackige Überschrift und der Preis.
Aktuell habe ich kein besonderes Grafikprogramm, nur paint.net. Sollte es günstige, geeignete Programme geben, die ich für die Bearbeitung benötige, dann würde ich mich über eine Info freuen.

```html
<!DOCTYPE html>
<html lang="en">
<head>
<meta charset="utf-8">
<title>Real Estate Ad – Nordhaus</title>
<link rel="stylesheet" href="https://fonts.googleapis.com/css2?family=Montserrat:wght@500;600;700;800&display=swap">
<style>
  :root {
    --blue: #1c6690;
    --yellow: #f4b400;
    --yellow-deep: #dfa52c;
    --white: #ffffff;
    --ink: #1d1d1d;
    --stage: #e4e4e4;
  }
  * { margin: 0; padding: 0; box-sizing: border-box; }
  html, body {
    width: 1024px; height: 1200px; overflow: hidden;
    background: var(--stage);
    font-family: "Montserrat", Arial, sans-serif;
  }
  .ad {
    position: absolute; left: 62px; top: 145px;
    width: 556px; height: 562px;
    background: var(--white);
    transform: scale(1.62); transform-origin: top left;
    overflow: hidden;
  }
  .side {
    position: absolute; left: 0; top: 0; width: 217px; height: 100%;
    background: var(--blue);
  }
  .headline {
    position: absolute; left: 15px; top: 44px;
    color: var(--white); font-weight: 800; font-size: 31px;
    line-height: 38px; letter-spacing: 0.5px;
  }
  .accent { color: var(--yellow); }
  .pitch {
    position: absolute; left: 14px; top: 233px; width: 195px;
    color: var(--white); font-weight: 700; font-size: 15px; line-height: 19px;
  }
  .pitch p { margin-bottom: 16px; }
  .cta {
    position: absolute; left: 14px; top: 395px; width: 175px; height: 41px;
    background: var(--yellow); color: var(--white);
    font-weight: 700; font-size: 20px; letter-spacing: 1px;
    display: flex; align-items: center; justify-content: center;
  }
  .corner { position: absolute; left: 217px; top: 0; }
  .brand {
    position: absolute; right: 20px; top: 30px;
    display: flex; align-items: center; gap: 6px;
    color: var(--ink); font-weight: 800; font-size: 24px; letter-spacing: -0.5px;
  }
  .brand-mark { width: 12px; height: 12px; background: var(--yellow); }
  .photo {
    position: absolute; left: 217px; top: 110px; width: 339px; height: 290px;
    background: linear-gradient(180deg, #4e9ccb 0%, #8fc1dd 42%, #7a4a32 58%, #3e3a34 74%, #5f7a3a 88%, #6c8a44 100%);
  }
  .price {
    position: absolute; left: 376px; top: 360px; width: 178px; height: 40px;
    background: var(--blue); color: var(--white);
    font-weight: 700; font-size: 22px;
    display: flex; align-items: center; justify-content: center;
  }
  .tagline {
    position: absolute; right: 15px; top: 418px;
    text-align: right; color: var(--ink);
    font-weight: 600; font-size: 14px; line-height: 18px;
  }
  .contact-bar {
    position: absolute; left: 14px; top: 470px; width: 527px; height: 77px;
    background: var(--yellow); color: var(--white);
    display: flex; align-items: center;
  }
  .agent { width: 240px; text-align: center; }
  .agent-name { font-weight: 700; font-size: 22px; letter-spacing: 0.5px; }
  .agent-role { font-weight: 600; font-size: 8px; letter-spacing: 0.5px; margin-top: 2px; }
  .divider { width: 2px; height: 52px; background: var(--white); }
  .details {
    margin-left: 36px; display: grid;
    grid-template-columns: 72px auto; row-gap: 2px;
    font-weight: 600; font-size: 11.5px; line-height: 16px;
  }
</style>
</head>
<body>
  <div class="ad">
    <div class="side">
      <h1 class="headline"><span class="accent">HOUSE</span> IS<br>WHERE<br>MEMORIES<br>GROW</h1>
      <div class="pitch">
        <p>Do you want to sell<br>your <span class="accent">house</span>?</p>
        <p>Do you want to buy<br>a <span class="accent">house</span>?</p>
        <p>I can help you</p>
      </div>
      <div class="cta">CALL NOW</div>
    </div>

    <svg class="corner" width="160" height="110" viewBox="0 0 160 110">
      <polygon points="0,0 153,0 78,55 0,55" fill="var(--yellow)"/>
      <polygon points="0,55 78,55 152,110 0,110" fill="var(--yellow-deep)"/>
    </svg>

    <div class="brand"><span class="brand-mark"></span>Nordhaus</div>

    <div class="photo" role="img" aria-label="Photo of the house for sale: timber-framed house with red tiled roof under a blue sky, lawn in front"></div>
    <div class="price">€ 400,000</div>

    <p class="tagline">I'm an experienced Real Estate Agent<br>you can count on me</p>

    <div class="contact-bar">
      <div class="agent">
        <div class="agent-name">RONALD42</div>
        <div class="agent-role">REAL ESTATE AGENT</div>
      </div>
      <div class="divider"></div>
      <div class="details">
        <span>Phone</span><span>: 0361-555 20 48</span>
        <span>Office</span><span>: Lindenweg 7, 99084<br>&nbsp;&nbsp;Erfurt Germany</span>
      </div>
    </div>
  </div>
</body>
</html>
```